Book Cover for Self Help Book Teens

I need a standard a5 size book cover (front and back) for my new self help book for teens. The book is called
WHEN DAYS DRAG
ideas and tactics for teens in tough times
break ups, school problems, procrastination, fights, sexuality, alcohol, bitchiness, eating problems, can’t sleep, no motivation, not allowed to do stuff, being on the outer..and 34 other common situations that every day Australian teens face
Marisol Penhale
psychologist for teens
I would like a very sparse,very modern cover, no photos - maybe just cartoon-y graphic of smiley face upside down - ie frowny face. Few colours in order to make it look bold. lots of space on the cover.
I will provide back cover text soon
Updates
I just want to say that I really appreciate all of your efforts, the designs were excellent. As a thankyou, I'm happy to email you a link to the e-version of this book if you are interested. Just email me at marisolpenhale@brightwavemail.net and I will send it through as soon as it is completed.
Target Market(s)
teens....but parents will also be buying book
Industry/Entity Type
School
Look and feel

```html
<!DOCTYPE html>
<html lang="en">
<head>
<meta charset="utf-8">
<title>When Days Drag – Book Cover</title>
<link rel="stylesheet" href="https://fonts.googleapis.com/css2?family=Questrial&display=swap">
<style>
  :root {
    --paper: #ffffff;
    --title-ink: #5a2440;
    --title-echo: #f2a9c9;
    --subtitle-ink: #b25c8a;
    --subtitle-echo: #f6cfe0;
    --rule: #b25c8a;
    --author-ink: #1b2a6e;
    --role-ink: #5a6cad;
  }
  * { margin: 0; padding: 0; box-sizing: border-box; }
  html, body {
    width: 887px;
    height: 1200px;
    overflow: hidden;
    background: var(--paper);
  }
  .cover {
    position: relative;
    width: 887px;
    height: 1200px;
    background: var(--paper);
    font-family: "Questrial", "Century Gothic", sans-serif;
  }
  .title-block {
    position: absolute;
    left: 53px;
    top: 278px;
    width: 790px;
  }
  .book-title {
    font-weight: 400;
    font-size: 70px;
    line-height: 1;
    letter-spacing: 1px;
    color: var(--title-ink);
    text-shadow: 4px -3px 0 var(--title-echo);
    white-space: nowrap;
  }
  .book-subtitle {
    margin-top: 2px;
    padding-left: 14px;
    font-size: 34px;
    line-height: 1.1;
    letter-spacing: 0.5px;
    color: var(--subtitle-ink);
    text-shadow: 2px -2px 0 var(--subtitle-echo);
    white-space: nowrap;
  }
  .title-rule {
    position: absolute;
    left: 43px;
    top: 406px;
    width: 795px;
    height: 1px;
    background: var(--rule);
  }
  .author-block {
    position: absolute;
    right: 28px;
    top: 1040px;
    text-align: left;
  }
  .author-name {
    font-size: 64px;
    line-height: 1;
    color: var(--author-ink);
    white-space: nowrap;
  }
  .author-role {
    margin-top: 4px;
    padding-left: 10px;
    font-size: 33px;
    line-height: 1.1;
    color: var(--role-ink);
    white-space: nowrap;
  }
</style>
</head>
<body>
  <main class="cover">
    <header class="title-block">
      <h1 class="book-title">WHEN DAYS DRAG</h1>
      <p class="book-subtitle">ideas and tactics for teens in tough times</p>
    </header>
    <div class="title-rule" aria-hidden="true"></div>
    <footer class="author-block">
      <p class="author-name">Marisol Penhale</p>
      <p class="author-role">psychologist for teens</p>
    </footer>
  </main>
</body>
</html>
```